Marketing Collateral Template Design

We are in the middle of rebranding and rolling out a new webiste. We would like to create collateral templates that match our new brand and style guide and are visually appealing to clients. The templates include:
- flyer one-pagers (data sheets)
- case studies
- whitepaper

We have the colors, font and basic design look/feel we want to use, we just need someone to leverage those elements and create templates that have a similar design but are unique as well (ie we want someone looking at a data sheet and a case study to know they are different materials, but from the same brand).

Primary Colors:
Darker BLUE (Red: 19 / Green: 67 / Blue: 113)
BLUE (Red: 15 / Green: 111 / Blue: 161)
Lighter BLUE (Red: 137 / Green: 153 / Blue: 228)

Font:
Headers: Gotham, Light
Body: Gotham, Book

Requirements
Must have
• Primary Colors:

Font:
Headers: Gotham, Light
Body: Gotham, Book
Should not have
• the templates should not have too much text

```html
<!DOCTYPE html>
<html lang="en">
<head>
<meta charset="utf-8">
<title>Company Name – Flyer</title>
<link rel="stylesheet" href="https://fonts.googleapis.com/css2?family=Montserrat:wght@300;400;500&display=swap">
<style>
  :root {
    --blue-dark: #134371;
    --blue: #0f6fa1;
    --blue-light: #8999e4;
    --orange: #f26b2a;
    --orange-warm: #f7941d;
    --orange-soft: #fbb040;
    --ink: #1a1a1a;
    --white: #ffffff;
  }
  * { margin: 0; padding: 0; box-sizing: border-box; }
  html, body { width: 847px; height: 1200px; overflow: hidden; background: var(--white); }
  body { font-family: "Montserrat", sans-serif; color: var(--ink); }
  .flyer { position: relative; width: 847px; height: 1200px; overflow: hidden; background: var(--white); }

  .header-band { position: absolute; left: 0; top: 0; width: 847px; height: 170px; }
  .company-title {
    position: absolute; left: 40px; top: 30px;
    font-weight: 300; font-size: 60px; color: var(--white); letter-spacing: 0.5px;
  }

  .hero-photo {
    position: absolute; left: 290px; top: 143px; width: 557px; height: 400px;
    background:
      linear-gradient(90deg, rgba(255,255,255,1) 0%, rgba(255,255,255,0.55) 22%, rgba(255,255,255,0) 50%),
      linear-gradient(180deg, rgba(255,255,255,0) 70%, rgba(255,255,255,0.9) 100%),
      radial-gradient(ellipse at 62% 40%, #3c4a52 0%, #1f2a31 45%, #4d6870 80%, #8ab0b4 100%);
  }

  .headline {
    position: absolute; left: 40px; top: 186px; width: 400px;
    font-weight: 300; font-size: 40px; line-height: 50px; color: var(--ink);
  }

  .offer-badges { position: absolute; left: 30px; top: 345px; width: 260px; height: 240px; }
  .offer-text {
    position: absolute; left: 36px; top: 362px; width: 146px;
    text-align: center; color: var(--white); font-size: 26px; line-height: 32px; font-weight: 400;
  }

  .divider-top { position: absolute; left: 0; top: 530px; width: 847px; height: 80px; }

  .intro-quote {
    position: absolute; left: 40px; top: 590px; width: 374px;
    font-size: 18.5px; line-height: 31px; text-align: justify; hyphens: auto;
  }

  .feature-list { position: absolute; left: 440px; top: 590px; width: 395px; list-style: none; }
  .feature { display: flex; align-items: center; height: 111px; }
  .feature-icon { flex: 0 0 76px; width: 76px; height: 76px; margin-right: 24px; }
  .feature-text { font-size: 14.5px; line-height: 16px; text-align: justify; }

  .footer-band { position: absolute; left: 0; top: 1030px; width: 847px; height: 170px; }
  .contact {
    position: absolute; left: 38px; top: 1074px;
    color: var(--white); font-size: 30px; line-height: 37px; font-weight: 300;
  }
  .address {
    position: absolute; right: 30px; top: 1066px;
    color: var(--white); font-size: 25px; line-height: 29px; text-align: right; font-weight: 300;
  }
</style>
</head>
<body>
<main class="flyer">

  <svg class="header-band" viewBox="0 0 847 170" aria-hidden="true">
    <defs>
      <linearGradient id="headerFill" x1="0" y1="0" x2="1" y2="0">
        <stop offset="0" stop-color="#1a5f95"/>
        <stop offset="1" stop-color="#134371"/>
      </linearGradient>
    </defs>
    <rect x="0" y="0" width="847" height="138" fill="url(#headerFill)"/>
    <polyline points="0,141 400,141 424,163 448,141 847,141" fill="none" stroke="var(--orange)" stroke-width="4"/>
  </svg>
  <h1 class="company-title">Company Name</h1>

  <div class="hero-photo" role="img" aria-label="Photo of a person working at a laptop in a high-tech workshop"></div>

  <h2 class="headline">Text here to explain the purpose of the flyer</h2>

  <svg class="offer-badges" viewBox="0 0 260 240" aria-hidden="true">
    <polygon points="42,0 122,0 162,73 122,146 42,146 2,73" fill="var(--orange-warm)"/>
    <polygon points="168,130 212,130 234,170 212,210 168,210 146,170" fill="var(--orange-soft)"/>
  </svg>
  <p class="offer-text">Offer/<br>Call to<br>Action</p>

  <svg class="divider-top" viewBox="0 0 847 80" aria-hidden="true">
    <polyline points="0,44 398,44 424,68 450,44 847,44" fill="none" stroke="var(--orange)" stroke-width="4"/>
  </svg>

  <p class="intro-quote">"Lorem ipsum dolor sit amet, consectetur adipisicing elit, sed do eiusmod tempor incididunt ut labore et dolore magna aliqua. Ut enim ad minim veniam, quis nostrud exercitation ullamco laboris nisi ut aliquip ex ea commodo consequat. Duis aute irure dolor in reprehenderit in voluptate velit esse cillum dolore eu fugiat nulla pariatur. Excepteur sint occaecat cupidatat non proident, sunt in culpa qui officia deserunt mollit anim id est laborum."</p>

  <ul class="feature-list">
    <li class="feature">
      <svg class="feature-icon" viewBox="0 0 76 76" aria-hidden="true">
        <circle cx="38" cy="38" r="38" fill="var(--blue-dark)"/>
        <ellipse cx="38" cy="38" rx="17" ry="10" fill="var(--white)"/>
      </svg>
      <p class="feature-text">Lorem ipsum dolor sit amet, consectetur adipisicing elit, sed do eiusmod tempor incididunt ut labore et dolore magna aliqua</p>
    </li>
    <li class="feature">
      <svg class="feature-icon" viewBox="0 0 76 76" aria-hidden="true">
        <circle cx="38" cy="38" r="38" fill="var(--blue)"/>
        <rect x="24" y="24" width="28" height="28" fill="var(--white)"/>
      </svg>
      <p class="feature-text">Lorem ipsum dolor sit amet, consectetur adipisicing elit, sed do eiusmod tempor incididunt ut labore et dolore magna aliqua</p>
    </li>
    <li class="feature">
      <svg class="feature-icon" viewBox="0 0 76 76" aria-hidden="true">
        <circle cx="38" cy="38" r="38" fill="var(--blue-light)"/>
        <polygon points="38,20 56,50 20,50" fill="var(--white)"/>
      </svg>
      <p class="feature-text">Lorem ipsum dolor sit amet, consectetur adipisicing elit, sed do eiusmod tempor incididunt ut labore et dolore magna aliqua</p>
    </li>
    <li class="feature">
      <svg class="feature-icon" viewBox="0 0 76 76" aria-hidden="true">
        <circle cx="38" cy="38" r="38" fill="var(--blue-dark)"/>
        <polygon points="38,19 43,33 58,33 46,42 50,56 38,48 26,56 30,42 18,33 33,33" fill="var(--white)"/>
      </svg>
      <p class="feature-text">Lorem ipsum dolor sit amet, consectetur adipisicing elit, sed do eiusmod tempor incididunt ut labore et dolore magna aliqua</p>
    </li>
  </ul>

  <svg class="footer-band" viewBox="0 0 847 170" aria-hidden="true">
    <defs>
      <linearGradient id="footerFill" x1="0" y1="0" x2="1" y2="0">
        <stop offset="0" stop-color="#1a5f95"/>
        <stop offset="1" stop-color="#134371"/>
      </linearGradient>
    </defs>
    <polygon points="0,22 398,22 424,0 450,22 847,22 847,170 0,170" fill="url(#footerFill)"/>
    <polyline points="0,22 398,22 424,0 450,22 847,22" fill="none" stroke="var(--orange)" stroke-width="4"/>
  </svg>
  <address class="contact" style="font-style: normal;">
    T: 01234 678 9101<br>
    E: info@companyname.com<br>
    W: www.companyname.com
  </address>
  <address class="address" style="font-style: normal;">
    Company Name<br>
    Address 1<br>
    Address 2<br>
    Zip Code
  </address>

</main>
</body>
</html>
```